How To Guide for Licensing Pet

3.5" x 2.5" playing card size. Two sided design, color is alright. Front side, City of Davenport Pet License, and back side would be City of Bettendorf Dog License.
*Note both cities have different licensing requirements, dates and pricing.

Local License Fees
The City of Davenport requires that all dogs and cats be licensed over the age of 6 months. Pet owners must purchase a license for their pet within thirty days of the date the pet is initially given the rabies vaccine and annually within thirty days’ time of the date of the current rabies vaccination. Licenses can be purchased at the Humane Society of Marlow Ridge with verification of a current rabies vaccination signed and administered by a licensed veterinarian.

Annual license fees are:

Neutered/spayed (altered) dog or cat – $10
Non-altered dog or cat – $30

To License: Current identification & current rabies vaccination certificate and bring to Humane Society of Marlow Ridge
4517 E Linden Grove Rd
Davenport, IA 52804
563-555-0147

-
The City of Bettendorf requires every dog over 6 months of age be licensed. Licenses can be purchased at the Humane Society of Marlow Ridge . Pet licenses must be purchased prior to January 31 of each calendar year. Pet owners applying for a license must present a certificate of current rabies vaccination signed and administered by a licensed veterinarian.

Annual license fees are:

Neutered/spayed (altered) dog – $3
Non-altered dog – $25

4517 E Linden Grove Rd
Davenport, IA 52804
563-555-0147

Target Market(s)

Animal Owners, easy to read

Industry/Entity Type

Pet

Requirements
Must have
• SIZE: 3.5" x 2.5" Playing Card Size
2 sides, Front: Davenport, Back: Bettendorf.
Bettendorf only has Dog License requirement*

```html
<!DOCTYPE html>
<html lang="en">
<head>
<meta charset="utf-8">
<title>Pet License Guide Cards</title>
<link href="https://fonts.googleapis.com/css2?family=Russo+One&family=Source+Sans+3:ital,wght@0,400;0,600;0,700;1,600;1,700&display=swap" rel="stylesheet">
<style>
  :root {
    --purple: #92278f;
    --navy: #2b3990;
    --yellow: #ffde17;
    --ink: #231f20;
    --white: #ffffff;
    --tan: #c2b59b;
    --tan-light: #d8ccb4;
    --sky: #bfe4f7;
    --fur: #9a8370;
  }
  * { box-sizing: border-box; margin: 0; padding: 0; }
  html, body { width: 1200px; height: 1000px; overflow: hidden; }
  body {
    position: relative;
    background: radial-gradient(ellipse at 50% 50%, #ffffff 0%, #e6e7e8 55%, #cfd0d2 100%);
    font-family: "Source Sans 3", "Myriad Pro", sans-serif;
    color: var(--ink);
  }
  .card {
    position: absolute;
    background: var(--white);
    border: 1px solid #8a8a8a;
    overflow: hidden;
  }
  .card--davenport { left: 19px; top: 12px; width: 661px; height: 473px; }
  .card--bettendorf { left: 518px; top: 508px; width: 662px; height: 472px; }

  .card__header {
    position: absolute; left: 0; top: 0; width: 100%; height: 65px;
    display: flex; align-items: center; justify-content: center;
  }
  .card--davenport .card__header { background: var(--purple); }
  .card--bettendorf .card__header { background: var(--navy); }
  .card__title {
    font-family: "Russo One", sans-serif;
    font-style: italic;
    font-weight: 400;
    font-size: 37px;
    color: var(--yellow);
    text-shadow: 2px 2px 0 #1a1a1a;
    white-space: nowrap;
  }
  .card__subtitle {
    position: absolute; left: 16px; top: 67px;
    font-weight: 700; font-style: italic; font-size: 25px; line-height: 32px;
  }
  .card__body {
    position: absolute; text-align: justify;
    font-size: 18.6px; line-height: 21px; letter-spacing: 0.3px;
  }
  .card--davenport .card__body { left: 16px; top: 104px; width: 631px; }
  .card--bettendorf .card__body { left: 16px; top: 72px; width: 632px; }
  .card__body strong { font-weight: 700; }

  .fees__banner { position: absolute; left: 0; height: 50px; width: 410px; }
  .card--davenport .fees__banner { top: 266px; }
  .card--bettendorf .fees__banner { top: 271px; }
  .fees__banner svg { position: absolute; inset: 0; }
  .fees__label {
    position: absolute; left: 16px; top: 11px;
    font-weight: 700; font-style: italic; font-size: 21px; color: var(--yellow);
  }
  .fees__list {
    position: absolute; left: 16px; list-style: none; width: 356px;
    font-weight: 700; font-style: italic; font-size: 17.5px; line-height: 23px;
  }
  .card--davenport .fees__list { top: 320px; }
  .card--bettendorf .fees__list { top: 325px; }
  .fees__item { display: flex; justify-content: space-between; }

  .card__footer {
    position: absolute; left: 0; bottom: 0; width: 100%; height: 97px;
    background: var(--ink); color: var(--white);
    padding: 3px 0 0 16px; font-size: 13px; line-height: 16px; letter-spacing: 0.2px;
  }
  .card__footer em { font-weight: 700; font-style: italic; }

  .art { position: absolute; }
  .art--pets {
    left: 390px; top: 236px; width: 266px; height: 140px;
    background: linear-gradient(135deg, var(--tan-light), var(--tan));
  }
  .art--dog {
    left: 424px; top: 184px; width: 206px; height: 206px; border-radius: 50%;
    background: radial-gradient(circle at 50% 50%, var(--fur) 0%, #b7a797 55%, var(--sky) 100%);
  }
</style>
</head>
<body>

<section class="card card--davenport">
  <header class="card__header"><h1 class="card__title">City of Davenport Pet License</h1></header>
  <h2 class="card__subtitle">Local License Fees</h2>
  <p class="card__body"><strong>The City of Davenport requires that all dogs and cats be licensed over the age of 6 months.</strong> Pet owners must purchase a license for their pet within thirty days of the date the pet is initially given the rabies vaccine and annually within thirty days’ time of the date of the current rabies vaccination. Licenses can be purchased at the Humane Society of Marlow Ridge with verification of a current rabies vaccination signed and administered by a licensed veterinarian.</p>

  <div class="art art--pets" role="img" aria-label="Illustration of a dog and a cat in profile, facing opposite ways"></div>

  <div class="fees__banner">
    <svg width="410" height="50" viewBox="0 0 410 50"><polygon points="0,0 410,0 385,50 0,50" fill="var(--purple)"/></svg>
    <span class="fees__label">Annual License Fees Are:</span>
  </div>
  <ul class="fees__list">
    <li class="fees__item"><span>Neutered/spayed (altered) dog or cat</span><span>$10</span></li>
    <li class="fees__item"><span>Non-altered dog or cat</span><span>$30</span></li>
  </ul>

  <footer class="card__footer">
    <p><em>To License:</em> Current identification &amp; current rabies vaccination<br>certificate and bring to Humane Society of Marlow Ridge<br>4517 E Linden Grove Rd<br>Davenport, IA 52804<br>563-555-0147</p>
  </footer>
</section>

<section class="card card--bettendorf">
  <header class="card__header"><h1 class="card__title">City of Bettendorf Dog License</h1></header>
  <p class="card__body"><strong>The City of Bettendorf requires every dog over 6 months of age be licensed.</strong> Licenses can be purchased at the Humane Society of Marlow Ridge or from Bettendorf City Hall. Pet licenses must be purchased prior to January 31 of each calendar year. Pet owners applying for a license must present a certificate of current rabies vaccination signed and administered by a licensed veterinarian.</p>

  <div class="art art--dog" role="img" aria-label="Illustration of a dog's head in front of a light blue circle"></div>

  <div class="fees__banner">
    <svg width="410" height="50" viewBox="0 0 410 50"><polygon points="0,0 410,0 385,50 0,50" fill="var(--navy)"/></svg>
    <span class="fees__label">Annual License Fees Are:</span>
  </div>
  <ul class="fees__list">
    <li class="fees__item"><span>Neutered/spayed (altered) dog</span><span>$3</span></li>
    <li class="fees__item"><span>Non-altered dog</span><span>$25</span></li>
  </ul>

  <footer class="card__footer">
    <p><em>To License:</em> Current identification &amp; current rabies vaccination<br>certificate and bring to Humane Society of Marlow Ridge<br>4517 E Linden Grove Rd<br>Davenport, IA 52804<br>563-555-0147</p>
  </footer>
</section>

</body>
</html>
```